Endocrinologist needs new stationery

I have a logo from MarkForge and now need stationery with the new logo.

Address: Suite 4, 282 Falcon Street, Richmond, VIC 3121
Phone: 03 9417 2253
Fax: 03 9417 2255
Website: www.drmaylacorwen.com.au
Email: admin@drmaylacorwen.com.au

```html
<!DOCTYPE html>
<html lang="en">
<head>
<meta charset="utf-8">
<title>Dr Mayla Corwen – Stationery</title>
<link rel="stylesheet" href="https://fonts.googleapis.com/css2?family=Open+Sans:wght@400;600&display=swap">
<style>
  :root{
    --bg:#e7e5e1;
    --paper:#ffffff;
    --plum:#6f4a60;
    --brand-blue:#4b7db3;
    --ink:#4a4a4a;
    --text:#555555;
    --rule:#c9c2c6;
    --font:"Open Sans", Arial, sans-serif;
  }
  *{box-sizing:border-box;margin:0;padding:0}
  html,body{width:1200px;height:1200px;overflow:hidden}
  body{background:var(--bg);font-family:var(--font);color:var(--ink);position:relative}

  .sheet{position:absolute;background:var(--paper);box-shadow:0 6px 18px rgba(0,0,0,.12);overflow:hidden}

  /* name set in the text font, one colour, one weight */
  .brand-name{font-family:var(--font);font-weight:400;color:var(--brand-blue);font-size:24px;letter-spacing:.5px;line-height:1.1;white-space:nowrap}
  .brand-name--light{color:#ffffff}

  /* contact list */
  .contact{list-style:none;font-size:11px;line-height:1.8;color:var(--ink)}
  .contact li{display:flex;align-items:center;gap:6px;white-space:nowrap}
  .contact svg{width:10px;height:10px;fill:var(--plum);flex:none}
  .contact--right li{justify-content:flex-end}

  /* letterhead */
  .letterhead{left:560px;top:30px;width:600px;height:1000px}
  .letterhead .contact{position:absolute;right:40px;top:36px}
  .letterhead .brand-name{position:absolute;left:48px;top:170px}
  .letter{position:absolute;left:48px;top:250px;width:504px;font-size:11.5px;line-height:1.65}
  .letter__date{text-transform:uppercase;margin-bottom:18px}
  .letter__salutation{margin-bottom:14px}
  .letter p{margin-bottom:14px}
  .letter__body{color:var(--text)}
  .letter__closing{margin-top:6px;margin-bottom:8px}
  .signature{width:150px;height:34px;border-radius:4px;background:linear-gradient(90deg,#e9dfe4,#f4eef1)}

  .band{position:absolute;left:0;bottom:0;width:100%}
  .band__url{position:absolute;right:24px;bottom:10px;color:#fff;font-size:12px;letter-spacing:.5px;white-space:nowrap}

  /* envelope */
  .envelope{left:40px;top:60px;width:480px;height:260px}
  .envelope .brand-name{position:absolute;left:30px;top:28px;font-size:20px}
  .envelope__return{position:absolute;left:30px;top:70px;font-size:10.5px;line-height:1.6;font-style:normal}
  .envelope .band__url{font-size:11px}

  /* business cards */
  .card{width:340px;height:200px}
  .card--front{left:40px;top:380px}
  .card--front .brand-name{position:absolute;left:22px;top:20px;font-size:19px}
  .card--front .contact{position:absolute;left:22px;top:60px;font-size:9.5px;line-height:1.7}
  .card--front .band__url{font-size:9.5px;right:14px;bottom:6px}

  .card--back{left:40px;top:620px;background:var(--plum)}
  .card--back .brand-name{position:absolute;left:50%;top:50%;transform:translate(-50%,-50%);font-size:22px}
</style>
</head>
<body>

<svg width="0" height="0" style="position:absolute" aria-hidden="true">
  <symbol id="icon-pin" viewBox="0 0 10 10"><path d="M5 0a3.5 3.5 0 0 0-3.5 3.5C1.5 6 5 10 5 10s3.5-4 3.5-6.5A3.5 3.5 0 0 0 5 0zm0 5a1.4 1.4 0 1 1 0-2.8A1.4 1.4 0 0 1 5 5z"/></symbol>
  <symbol id="icon-phone" viewBox="0 0 10 10"><path d="M2 0.5l1.6 0 .8 2.3-1 .8a5.5 5.5 0 0 0 3 3l.8-1 2.3.8 0 1.6c0 .6-.5 1-1 1A8.5 8.5 0 0 1 1 1.5c0-.5.4-1 1-1z"/></symbol>
  <symbol id="icon-fax" viewBox="0 0 10 10"><path d="M2.5 0h5v3h-5zM1 3.5h8a1 1 0 0 1 1 1V9H0V4.5a1 1 0 0 1 1-1zm2 3v1.5h4V6.5z"/></symbol>
  <symbol id="icon-mail" viewBox="0 0 10 10"><path d="M0 2h10v6H0zm1 .8 4 3 4-3z"/></symbol>
</svg>

<!-- Letterhead -->
<section class="sheet letterhead">
  <ul class="contact contact--right">
    <li>Suite 4, 282 Falcon Street <svg><use href="#icon-pin"/></svg></li>
    <li>Richmond, VIC 3121 <svg style="visibility:hidden"><use href="#icon-pin"/></svg></li>
    <li>03 9417 2253 <svg><use href="#icon-phone"/></svg></li>
    <li>03 9417 2255 <svg><use href="#icon-fax"/></svg></li>
    <li>admin@drmaylacorwen.com.au <svg><use href="#icon-mail"/></svg></li>
  </ul>

  <span class="brand-name">Dr Mayla Corwen</span>

  <article class="letter">
    <p class="letter__date">May 05,2026</p>
    <p class="letter__salutation">To the Former Company name:</p>
    <p class="letter__body">Lorem Ipsum is simply dummy text of the printing and typesetting industry. Lorem Ipsum has been the industry's standard dummy text ever since the 1500s, when an unknown printer took a galley of type and scrambled it to make a type specimen book. It has survived not only five centuries, but also the leap into electronic typesetting, remaining essentially unchanged. It was popularised in the 1960s with the release of Letraset sheets containing Lorem Ipsum passages, and more recently with desktop publishing software like Aldus PageMaker including versions of Lorem Ipsum. Lorem Ipsum is simply dummy text of the printing and typesetting industry.</p>
    <p class="letter__body">Lorem Ipsum has been the industry's standard dummy text ever since the 1500s, when an unknown printer took a galley of type and scrambled it to make a type specimen book. It has survived not only five centuries, but also the leap into electronic typesetting, remaining essentially unchanged. It was popularised in the 1960s with the release of Letraset sheets containing Lorem Ipsum passages, and more recently with desktop publishing software like Aldus PageMaker including versions of Lorem Ipsum.</p>
    <p class="letter__body">Lorem Ipsum is simply dummy text of the printing and typesetting industry. Lorem Ipsum has been the industry's standard dummy text ever since the 1500s, when an unknown printer took a galley of type and scrambled it to make a type specimen book. It has survived not only five centuries, but also the leap into electronic typesetting, remaining essentially unchanged. It was popularised in the 1960s with the release of Letraset sheets containing Lorem Ipsum passages, and more recently with desktop publishing software including versions of Lorem Ipsum.</p>
    <p class="letter__closing">Sincerely yours,</p>
    <div class="signature" role="img" aria-label="Handwritten signature of Dr Mayla Corwen"></div>
  </article>

  <svg class="band" width="600" height="60" viewBox="0 0 600 60" aria-hidden="true">
    <path d="M0 60V38h330q10 0 16-8l6-8q6-8 16-8H600v46z" fill="var(--plum)"/>
    <path d="M0 32h326q8 0 13-7l5-6q5-7 14-7H600" fill="none" stroke="var(--rule)" stroke-width="1"/>
  </svg>
  <span class="band__url">www.drmaylacorwen.com.au</span>
</section>

<!-- Envelope -->
<section class="sheet envelope">
  <span class="brand-name">Dr Mayla Corwen</span>
  <address class="envelope__return">Suite 4, 282 Falcon Street,<br>Richmond, VIC 3121</address>
  <svg class="band" width="480" height="44" viewBox="0 0 480 44" aria-hidden="true">
    <path d="M0 44V26h250q8 0 13-6l4-6q5-6 13-6H480v36z" fill="var(--plum)"/>
    <path d="M0 20h246q7 0 11-5l4-5q4-5 11-5H480" fill="none" stroke="var(--rule)" stroke-width="1"/>
  </svg>
  <span class="band__url">www.drmaylacorwen.com.au</span>
</section>

<!-- Business card front -->
<section class="sheet card card--front">
  <span class="brand-name">Dr Mayla Corwen</span>
  <ul class="contact">
    <li>Suite 4, 282 Falcon Street</li>
    <li>Richmond, VIC 3121</li>
    <li><svg><use href="#icon-phone"/></svg>03 9417 2253</li>
    <li><svg><use href="#icon-fax"/></svg>03 9417 2255</li>
    <li><svg><use href="#icon-mail"/></svg>admin@drmaylacorwen.com.au</li>
  </ul>
  <svg class="band" width="340" height="34" viewBox="0 0 340 34" aria-hidden="true">
    <path d="M0 34V22h150q6 0 10-5l3-4q4-5 10-5H340v26z" fill="var(--plum)"/>
  </svg>
  <span class="band__url">www.drmaylacorwen.com.au</span>
</section>

<!-- Business card back -->
<section class="sheet card card--back">
  <span class="brand-name brand-name--light">Dr Mayla Corwen</span>
</section>

</body>
</html>
```